Creative Businesss Card desgin!

Create a business card for our business Gleam window cleaning!
We are open to creative ideas as long as it maintains a professional image.

Target Market(s)

Small Commercial window cleaning clients including car dealerships, strata manager, cafe

Industry/Entity Type

Window Cleaning

Contact Information for Business Card

Daniel Prescott
General Manager
Gleam Window Cleaning

daniel@gleamservices.com.au
pane-care-southbank.com.au
Ph: 1800 GET GLEAM
Mob: 0437 582 061

Colors
fbed22
0392cd

Requirements
Should not have
• Stock window cleaning/ squeegee graphics

```html
<!DOCTYPE html>
<html lang="en">
<head>
<meta charset="UTF-8">
<title>Gleam Window Cleaning – Business Card</title>
<link rel="stylesheet" href="https://fonts.googleapis.com/css2?family=Lato:wght@400;700;900&display=swap">
<style>
  :root {
    --bg: #2b2b2d;
    --blue-deep: #1c5a8f;
    --blue-mid: #2d6da3;
    --blue-light: #3f80b4;
    --navy: #1f4f80;
    --yellow: #e6ea2a;
    --paper: #f4f5f6;
    --paper-shade: #e3e5e8;
    --ink: #2a2f36;
    --rule: #c9d3de;
  }
  * { margin: 0; padding: 0; box-sizing: border-box; }
  html, body {
    width: 1200px; height: 997px; overflow: hidden;
    background: var(--bg);
    font-family: "Lato", sans-serif;
  }
  .canvas { position: relative; width: 1200px; height: 997px; }

  .card {
    position: absolute;
    width: 600px; height: 343px;
    overflow: hidden;
    box-shadow: 0 18px 40px rgba(0,0,0,.45);
  }

  /* Front */
  .card--front { left: 110px; top: 110px; }
  .front-texture {
    position: absolute; inset: 0;
    background: linear-gradient(135deg, var(--blue-light) 0%, var(--blue-mid) 45%, var(--blue-deep) 100%);
  }
  .front-brand {
    position: absolute; left: 0; right: 0; top: 104px;
    text-align: center; color: var(--yellow);
    font-weight: 900; line-height: 1;
  }
  .front-brand .brand-name { display: block; font-size: 78px; letter-spacing: 4px; }
  .front-brand .brand-tag { display: block; font-size: 26px; letter-spacing: 1.5px; margin-top: 6px; }
  .front-web {
    position: absolute; left: 0; right: 0; bottom: 34px;
    text-align: center; color: #dfe8f1;
    font-size: 14px; font-weight: 700; letter-spacing: 3px;
  }

  /* Back */
  .card--back { left: 490px; top: 520px; background: linear-gradient(180deg, var(--paper), var(--paper-shade)); }
  .back-band { position: absolute; left: 0; top: 0; width: 600px; height: 343px; }
  .back-brand {
    position: absolute; left: 220px; top: 26px; width: 340px;
    text-align: center; color: var(--yellow);
    font-weight: 900; line-height: 1;
  }
  .back-brand .brand-name { display: block; font-size: 52px; letter-spacing: 3px; }
  .back-brand .brand-tag { display: block; font-size: 18px; letter-spacing: 1px; margin-top: 4px; }

  .person {
    position: absolute; right: 330px; top: 232px; text-align: right;
  }
  .person-name { color: var(--navy); font-size: 24px; font-weight: 700; }
  .person-role { color: var(--ink); font-size: 15px; margin-top: 2px; }

  .divider {
    position: absolute; left: 290px; top: 196px; width: 2px; height: 104px;
    background: linear-gradient(180deg, transparent, var(--navy) 30%, var(--navy) 70%, transparent);
  }

  .contacts { position: absolute; left: 310px; top: 206px; list-style: none; }
  .contact { display: flex; align-items: center; gap: 10px; height: 29px; color: var(--ink); font-size: 15.5px; }
  .contact-icon { width: 22px; height: 22px; flex: none; }
</style>
</head>
<body>
<main class="canvas">

  <section class="card card--front" aria-label="Business card front">
    <div class="front-texture" role="img" aria-label="Blue faceted low-poly background texture"></div>
    <div class="front-brand">
      <span class="brand-name">GLEAM</span>
      <span class="brand-tag">WINDOW CLEANING</span>
    </div>
    <p class="front-web">www.pane-care-southbank.com.au</p>
  </section>

  <section class="card card--back" aria-label="Business card back">
    <svg class="back-band" viewBox="0 0 600 343" aria-hidden="true">
      <path d="M0 0 H600 V120 Q330 150 0 208 Z" fill="var(--blue-deep)"/>
      <path d="M0 214 Q330 156 600 126" fill="none" stroke="var(--navy)" stroke-width="2.5"/>
      <path d="M0 222 Q330 164 600 134" fill="none" stroke="var(--navy)" stroke-width="2.5"/>
      <path d="M0 230 Q330 172 600 142" fill="none" stroke="var(--navy)" stroke-width="2.5"/>
    </svg>

    <div class="back-brand">
      <span class="brand-name">GLEAM</span>
      <span class="brand-tag">WINDOW CLEANING</span>
    </div>

    <div class="person">
      <p class="person-name">Daniel Prescott</p>
      <p class="person-role">General Manager</p>
    </div>

    <div class="divider"></div>

    <ul class="contacts">
      <li class="contact">
        <svg class="contact-icon" viewBox="0 0 22 22" aria-hidden="true">
          <circle cx="11" cy="11" r="11" fill="var(--navy)"/>
          <path d="M6 9 Q11 5 16 9 L15 10.5 L13 9.8 L12.6 8.6 Q11 8.2 9.4 8.6 L9 9.8 L7 10.5 Z M7.5 12 H14.5 L15.5 16 H6.5 Z" fill="#fff"/>
        </svg>
        1800 GET GLEAM
      </li>
      <li class="contact">
        <svg class="contact-icon" viewBox="0 0 22 22" aria-hidden="true">
          <circle cx="11" cy="11" r="11" fill="var(--navy)"/>
          <rect x="7.5" y="5" width="7" height="12" rx="1.3" fill="none" stroke="#fff" stroke-width="1.4"/>
          <circle cx="11" cy="15" r=".8" fill="#fff"/>
        </svg>
        0437 582 061
      </li>
      <li class="contact">
        <svg class="contact-icon" viewBox="0 0 22 22" aria-hidden="true">
          <circle cx="11" cy="11" r="11" fill="var(--navy)"/>
          <rect x="5.5" y="7" width="11" height="8" fill="#fff"/>
          <path d="M5.5 7 L11 11.5 L16.5 7" fill="none" stroke="var(--navy)" stroke-width="1.2"/>
        </svg>
        daniel@gleamservices.com.au
      </li>
    </ul>
  </section>

</main>
</body>
</html>
```